Lotus Leaf Kitchen Road Billboard

Road Billboard I need all of this information on it
Authentic Thai Food Bangkok Style
6.5 Miles on the right
4126 Maple Ridge Rd Willowmere NC
828-555-4172

```html
<!DOCTYPE html>
<html lang="en">
<head>
<meta charset="utf-8">
<title>Lotus Leaf Kitchen Road Billboard</title>
<link href="https://fonts.googleapis.com/css2?family=Abril+Fatface&family=Poppins:wght@300;500;600;700&display=swap" rel="stylesheet">
<style>
  :root {
    --night: #0b0b0b;
    --charcoal: #222222;
    --gold: #d9ad1c;
    --signal-red: #f20d0d;
    --white: #ffffff;
    --ink: #2a2a2a;
  }
  html, body {
    margin: 0;
    padding: 0;
    width: 1200px;
    height: 667px;
    overflow: hidden;
    background: #ffffff;
  }
  .billboard {
    position: relative;
    width: 1200px;
    height: 667px;
    background: radial-gradient(ellipse at 35% 60%, var(--charcoal) 0%, var(--night) 75%);
    overflow: hidden;
  }
  .wok-photo {
    position: absolute;
    left: 640px;
    top: 0;
    width: 560px;
    height: 667px;
    background:
      radial-gradient(ellipse at 78% 32%, rgba(150,170,90,0.6) 0%, rgba(150,170,90,0) 30%),
      radial-gradient(ellipse at 28% 45%, rgba(250,150,40,0.95) 0%, rgba(210,85,15,0.65) 28%, rgba(0,0,0,0) 55%),
      radial-gradient(ellipse at 95% 92%, rgba(245,125,20,0.9) 0%, rgba(0,0,0,0) 32%),
      linear-gradient(90deg, rgba(11,11,11,1) 0%, rgba(25,16,10,0.9) 14%, #1a120c 100%);
  }
  .copy {
    position: absolute;
    inset: 0;
  }
  .headline-light { font-family: 'Poppins', sans-serif; font-weight: 300; fill: var(--white); }
  .headline-serif { font-family: 'Abril Fatface', serif; fill: var(--gold); }
  .headline-bold { font-family: 'Poppins', sans-serif; font-weight: 700; fill: var(--white); }
  .direction-text { font-family: 'Poppins', sans-serif; font-weight: 600; fill: var(--white); }
  .phone-text { font-family: 'Poppins', sans-serif; font-weight: 500; fill: var(--white); }
  .address-text { font-family: 'Poppins', sans-serif; font-weight: 500; fill: var(--ink); }
  .brand-name { font-family: 'Poppins', sans-serif; font-weight: 600; fill: var(--gold); }
</style>
</head>
<body>
<div class="billboard">
  <div class="wok-photo" role="img" aria-label="Shrimp, broccoli and vegetables tossed from a flaming wok"></div>

  <svg class="copy" width="1200" height="667" viewBox="0 0 1200 667">
    <defs>
      <linearGradient id="address-fill" x1="0" x2="1" y1="0" y2="0">
        <stop offset="0" stop-color="#d9ad1c" stop-opacity="0"/>
        <stop offset="0.1" stop-color="#d9ad1c" stop-opacity="1"/>
        <stop offset="1" stop-color="#d9ad1c"/>
      </linearGradient>
    </defs>

    <text class="headline-light" x="70" y="116" font-size="70" textLength="346" lengthAdjust="spacingAndGlyphs">Authentic</text>
    <text class="headline-serif" x="70" y="217" font-size="122" textLength="483" lengthAdjust="spacingAndGlyphs">Thai Food</text>
    <text class="headline-bold" x="70" y="281" font-size="66" textLength="483" lengthAdjust="spacingAndGlyphs">BANGKOK STYLE</text>

    <g class="direction-banner">
      <polygon points="69,302 502,302 536,340 502,378 69,378" fill="var(--signal-red)"/>
      <polygon points="511,302 534,302 568,340 534,378 511,378 545,340" fill="var(--white)"/>
      <polygon points="550,302 590,302 624,340 590,378 550,378 584,340" fill="var(--gold)"/>
      <text class="direction-text" x="94" y="352" font-size="38" textLength="403" lengthAdjust="spacingAndGlyphs">6.5 Miles on the right</text>
    </g>

    <g class="phone-line">
      <path d="M276 436 c-3 3 -3 8 1 14 c5 8 11 14 19 18 c5 3 9 2 12 -1 l3 -3 c1 -2 1 -3 -1 -5 l-7 -5 c-2 -1 -3 -1 -5 1 l-3 3 c-5 -2 -10 -7 -13 -12 l3 -3 c2 -2 2 -3 1 -5 l-5 -7 c-2 -2 -3 -2 -5 -1 z" fill="var(--gold)"/>
      <path d="M293 434 a9 9 0 0 1 9 9 M293 428 a15 15 0 0 1 15 15" stroke="var(--gold)" stroke-width="2" fill="none"/>
      <text class="phone-text" x="316" y="463" font-size="52" textLength="361" lengthAdjust="spacingAndGlyphs">828-555-4172</text>
    </g>

    <g class="address-line">
      <rect x="262" y="487" width="624" height="53" rx="26.5" fill="url(#address-fill)"/>
      <path d="M292 497 a12 12 0 0 1 12 12 c0 9 -12 22 -12 22 c0 0 -12 -13 -12 -22 a12 12 0 0 1 12 -12 z" fill="var(--white)"/>
      <circle cx="292" cy="509" r="4.5" fill="var(--gold)"/>
      <text class="address-text" x="316" y="527" font-size="44" textLength="539" lengthAdjust="spacingAndGlyphs">4126 Maple Ridge Rd Willowmere NC</text>
    </g>

    <g class="brand">
      <circle cx="166" cy="452" r="48" fill="none" stroke="var(--gold)" stroke-width="3"/>
      <text class="brand-name" x="166" y="538" font-size="21" text-anchor="middle" textLength="194" lengthAdjust="spacingAndGlyphs">Lotus Leaf Kitchen</text>
    </g>
  </svg>
</div>
</body>
</html>
```